" A Construtora BAVO nasceu para tornar o setor da construçao civil mais industrializado e SUSTENTAVEL!!! Trouxe ao Brasil o sistema construtivo que é utilizado nos Estados Unidos e Europa. Com soluçoes inovadoras para a construçao de casas, aliando tecnologia e eficiência em produtos e serviços, Nosso foco de trabalho é a construçao de residências e imóveis comerciais em Steel Frame. A estrutura da casa inteira é feita usando aço leve galvanizado e perfis metálicos revestidos na area externa com placa cimenticia e internamente com placa de drywall "

```html
<!DOCTYPE html>
<html lang="pt-BR">
<head>
<meta charset="utf-8">
<title>Construtora BAVO — Cartão de visita</title>
<link rel="stylesheet" href="https://fonts.googleapis.com/css2?family=Ubuntu:wght@400;500;700&display=swap">
<style>
  :root{
    --bg:#e9ecee;
    --brand-blue:#1a6a88;
    --brand-blue-dark:#135670;
    --brand-green:#7cc242;
    --ink:#4a4f55;
    --ink-soft:#6d737a;
    --card-white:#ffffff;
    --card-shade:#dfe3e6;
  }
  *{box-sizing:border-box;margin:0;padding:0}
  html,body{width:1200px;height:1200px;overflow:hidden}
  body{background:var(--bg);font-family:"Ubuntu",sans-serif;position:relative}

  .card{position:absolute;left:120px;width:960px;height:534px;border-radius:28px;overflow:hidden;
        box-shadow:0 14px 30px rgba(0,0,0,.18)}
  .card--back{top:44px;background:var(--brand-blue)}
  .card--front{top:622px;background:linear-gradient(180deg,var(--card-white) 0%,var(--card-white) 62%,var(--card-shade) 100%)}

  /* back */
  .back-mark{position:absolute;left:50%;top:50%;transform:translate(-50%,-50%);
             display:flex;align-items:center;gap:22px}
  .back-mark__square{width:58px;height:58px;background:var(--brand-green)}
  .back-mark__name{font-weight:700;font-size:88px;color:#fff;letter-spacing:2px}

  /* front */
  .person{position:absolute;left:100px;top:64px}
  .person__name{font-size:46px;font-weight:500;color:var(--ink);letter-spacing:.5px}
  .person__role{font-size:25px;color:var(--ink-soft);margin-top:6px}

  .contacts{position:absolute;left:70px;top:200px;list-style:none}
  .contacts li{display:flex;align-items:flex-start;gap:14px;font-size:27px;color:var(--ink);line-height:34px}
  .contacts svg{flex:0 0 22px;width:22px;height:22px;margin-top:6px;fill:var(--ink-soft)}

  .brand{position:absolute;right:70px;top:110px;display:flex;align-items:center;gap:20px}
  .brand__square{width:70px;height:70px;background:var(--brand-green)}
  .brand__name{font-weight:700;font-size:50px;color:var(--brand-blue-dark);line-height:1}

  .partner{position:absolute;right:60px;bottom:50px;display:flex;align-items:center;gap:14px}
  .partner__square{width:44px;height:44px;background:var(--brand-blue)}
  .partner__name{font-weight:500;font-size:36px;color:var(--brand-blue)}
</style>
</head>
<body>
  <section class="card card--back" aria-label="Verso do cartão">
    <div class="back-mark">
      <span class="back-mark__square"></span>
      <span class="back-mark__name">BAVO</span>
    </div>
  </section>

  <section class="card card--front" aria-label="Frente do cartão">
    <div class="person">
      <h1 class="person__name">Marcos Lima</h1>
      <p class="person__role">Diretor</p>
    </div>

    <ul class="contacts">
      <li><svg viewBox="0 0 24 24"><path d="M12 2a7 7 0 0 0-7 7c0 5 7 13 7 13s7-8 7-13a7 7 0 0 0-7-7zm0 9.5A2.5 2.5 0 1 1 12 6.5a2.5 2.5 0 0 1 0 5z"/></svg>
        <span>Rua das Acácias, 215 Jardim Sul<br>São Paulo &nbsp;SP</span></li>
      <li><svg viewBox="0 0 24 24"><path d="M6.6 10.8a15 15 0 0 0 6.6 6.6l2.2-2.2a1 1 0 0 1 1-.25 11.4 11.4 0 0 0 3.6.57 1 1 0 0 1 1 1V20a1 1 0 0 1-1 1A17 17 0 0 1 3 4a1 1 0 0 1 1-1h3.5a1 1 0 0 1 1 1c0 1.25.2 2.45.57 3.57a1 1 0 0 1-.25 1z"/></svg>
        <span>11 4000-1234</span></li>
      <li><svg viewBox="0 0 24 24"><path d="M7 2h10a2 2 0 0 1 2 2v16a2 2 0 0 1-2 2H7a2 2 0 0 1-2-2V4a2 2 0 0 1 2-2zm0 3v13h10V5zm5 14.2a1 1 0 1 0 0 .01z"/></svg>
        <span>11 4000-5678</span></li>
      <li><svg viewBox="0 0 24 24"><path d="M12 2a10 10 0 1 0 5 18.7l-1-1.7A8 8 0 1 1 20 12v1a2 2 0 0 1-4 0V7h-2v1a5 5 0 1 0 .6 7.4A4 4 0 0 0 22 13v-1A10 10 0 0 0 12 2zm0 13a3 3 0 1 1 0-6 3 3 0 0 1 0 6z"/></svg>
        <span>marcos@bavo.com.br</span></li>
      <li><svg viewBox="0 0 24 24"><path d="M4 2l14 8-6 1.5 4 7.5-2.5 1.3-4-7.5L5 17z"/></svg>
        <span>www.bavo.com.br</span></li>
    </ul>

    <div class="brand">
      <span class="brand__square"></span>
      <span class="brand__name">Construtora<br>BAVO</span>
    </div>

    <div class="partner">
      <span class="partner__square"></span>
      <span class="partner__name">LUMEN</span>
    </div>
  </section>
</body>
</html>
```